Australian Solar Smart Home Provider needs business card design

We need a simple, clean, business card that shows who we are and gives the brand feeling. Please see the website (www.pelvora.com) and the attached logo as well. Please use this logo on the business card. As a business we do residential solar, batteries, smart home technology, and hot water solutions. We want the feeling to be accessible to ages 40-65 but at the same time be a bit on the technologically savvy side.
Also the primary purpose of the business card is to hand of and drive referrals - so we want everyone to have a referral code on the card and that aspect should stand out.
Things we want on the card with an example employee:
Name: Brent Malvaney
Position: Director of Sales and Marketing
telephone number office: 02 8736 2914
telephone number mobile: 0478 591 830
address: Suite 403, 19 Clover Lane, Sydney, NSW 2000
website: www.pelvora.com
Target Market(s)
Homeowners aged 35-60
Industry/Entity Type
Residential
Contact Information for Business Card
Name: Brent Malvaney
website: www.pelvora.com
referral code: Bmalvaney
Look and feel

```html
<!DOCTYPE html>
<html lang="en">
<head>
<meta charset="utf-8">
<title>Pelvora Business Card</title>
<link rel="stylesheet" href="https://fonts.googleapis.com/css2?family=Questrial&display=swap">
<style>
  :root {
    --page-bg: #e6e6e4;
    --card-bg: #f7f7f6;
    --card-shade: #ececeb;
    --brand-green: #8cc63f;
    --text-grey: #8e9092;
    --logo-grey: #7d8083;
  }
  * { margin: 0; padding: 0; box-sizing: border-box; }
  html, body {
    width: 1200px;
    height: 1000px;
    overflow: hidden;
    background: var(--page-bg);
    font-family: "Questrial", "Century Gothic", sans-serif;
  }
  .business-card {
    position: absolute;
    left: 345px;
    top: 70px;
    width: 510px;
    height: 860px;
    background: linear-gradient(160deg, var(--card-bg) 0%, #ffffff 40%, var(--card-shade) 100%);
    box-shadow: 0 6px 24px rgba(0, 0, 0, 0.12);
  }
  .brand-lockup {
    position: absolute;
    top: 58px;
    right: 48px;
    display: flex;
    align-items: center;
    gap: 14px;
  }
  .brand-dot {
    width: 46px;
    height: 46px;
    border-radius: 50%;
    background: var(--brand-green);
  }
  .brand-name {
    font-size: 46px;
    color: var(--logo-grey);
    letter-spacing: -0.5px;
    line-height: 1;
  }
  .person {
    position: absolute;
    left: 56px;
    top: 400px;
  }
  .person-name {
    font-size: 30px;
    text-transform: uppercase;
    color: var(--text-grey);
    letter-spacing: 0.5px;
    font-weight: 400;
    line-height: 1.2;
  }
  .person-role {
    font-size: 23px;
    color: var(--brand-green);
    margin-top: 2px;
    line-height: 1.3;
  }
  .contact-list {
    position: absolute;
    left: 56px;
    top: 498px;
    list-style: none;
    display: grid;
    grid-template-columns: 30px auto;
    column-gap: 14px;
    row-gap: 10px;
    align-items: start;
  }
  .contact-item { display: contents; }
  .contact-icon {
    width: 24px;
    height: 26px;
    fill: var(--brand-green);
    margin-top: 2px;
  }
  .contact-text {
    font-size: 23px;
    line-height: 1.3;
    color: var(--text-grey);
  }
  .referral {
    position: absolute;
    left: 56px;
    right: 56px;
    bottom: 70px;
    padding: 16px 22px;
    border: 2px solid var(--brand-green);
    border-radius: 8px;
    display: flex;
    justify-content: space-between;
    align-items: baseline;
  }
  .referral-label {
    font-size: 20px;
    color: var(--text-grey);
    text-transform: uppercase;
    letter-spacing: 1px;
  }
  .referral-code {
    font-size: 28px;
    color: var(--brand-green);
  }
</style>
</head>
<body>
  <section class="business-card">
    <div class="brand-lockup">
      <span class="brand-dot"></span>
      <span class="brand-name">pelvora</span>
    </div>

    <div class="person">
      <h1 class="person-name">Brent Malvaney</h1>
      <p class="person-role">Director of Sales and Marketing</p>
    </div>

    <ul class="contact-list">
      <li class="contact-item">
        <svg class="contact-icon" viewBox="0 0 24 26" aria-hidden="true">
          <path d="M12 1a8 8 0 0 0-8 8c0 6 8 15 8 15s8-9 8-15a8 8 0 0 0-8-8zm0 11a3 3 0 1 1 0-6 3 3 0 0 1 0 6z"/>
        </svg>
        <span class="contact-text">Suite 403, 19 Clover Lane,<br>Sydney, NSW 2000</span>
      </li>
      <li class="contact-item">
        <svg class="contact-icon" viewBox="0 0 24 26" aria-hidden="true">
          <path d="M6 3l4 4-2 3c1 3 4 6 7 7l3-2 4 4-3 4C10 22 3 15 2 6z"/>
        </svg>
        <span class="contact-text">02 8736 2914</span>
      </li>
      <li class="contact-item">
        <svg class="contact-icon" viewBox="0 0 24 26" aria-hidden="true">
          <path d="M7 2h10a2 2 0 0 1 2 2v18a2 2 0 0 1-2 2H7a2 2 0 0 1-2-2V4a2 2 0 0 1 2-2zm0 3v14h10V5zm5 15.5a1.2 1.2 0 1 0 0 2.4 1.2 1.2 0 0 0 0-2.4z"/>
        </svg>
        <span class="contact-text">0478 591 830</span>
      </li>
      <li class="contact-item">
        <svg class="contact-icon" viewBox="0 0 24 26" aria-hidden="true">
          <path d="M12 2a11 11 0 1 0 0 22 11 11 0 0 0 0-22zm7.8 10h-3.9a17 17 0 0 0-1.3-7A9 9 0 0 1 19.8 12zM12 4.3c1 1.4 1.8 4 1.9 7.7h-3.8C10.2 8.3 11 5.7 12 4.3zM9.4 5a17 17 0 0 0-1.3 7H4.2A9 9 0 0 1 9.4 5zM4.2 14h3.9a17 17 0 0 0 1.3 7A9 9 0 0 1 4.2 14zm7.8 7.7c-1-1.4-1.8-4-1.9-7.7h3.8c-.1 3.7-.9 6.3-1.9 7.7zm2.6-.7a17 17 0 0 0 1.3-7h3.9a9 9 0 0 1-5.2 7z"/>
        </svg>
        <span class="contact-text">www.pelvora.com</span>
      </li>
    </ul>

    <div class="referral">
      <span class="referral-label">Referral code</span>
      <span class="referral-code">Bmalvaney</span>
    </div>
  </section>
</body>
</html>
```